Letterhead for a German Distribution/Manufacturing Company

We need a professional Letterhead in a unique Design.
not to playful.
The Letterhead has to show show that we are a international company with headquater in Germany.
all details like adress, Vat Tax Number, Bank Accout, Eori, email, Company number has to be on the Letterhead.
for example use: VAT TAX DE5704168 Bank Account: Norrfeld Bank IBAN DE421705238ß310482 Swift: KOLV3154802 EORI 3041296587 Company Number: HRB 61508 Adress: VOLTRINA UG Amsel Strasse 7 Postal Code 04683 City Halvenstedt Country: Germany Email: info@voltrina-example.com
the design can be colored but doesnt have to be
Industry/Entity Type
Manufacturing and international distribution
Requirements
Must have
- show that we are a international company with headquater in Germany. our company infos and logo

```html
<!DOCTYPE html>
<html lang="en">
<head>
<meta charset="utf-8">
<title>VOLTRINA Letterhead</title>
<link rel="stylesheet" href="https://fonts.googleapis.com/css2?family=Arimo:wght@400;700&display=swap">
<style>
  :root {
    --backdrop: #c9c9c9;
    --paper: #ffffff;
    --label: #a3a3a3;
    --value: #5a5a5a;
    --brand: #6b6b6b;
    --watermark: #ededed;
  }
  html, body {
    margin: 0;
    padding: 0;
    width: 1200px;
    height: 960px;
    overflow: hidden;
    background: var(--backdrop);
    font-family: "Arimo", Helvetica, Arial, sans-serif;
  }
  .sheet {
    position: absolute;
    left: 280px;
    top: 28px;
    width: 640px;
    height: 904px;
    background: var(--paper);
    box-shadow: 0 2px 10px rgba(0,0,0,0.12);
  }
  .brand {
    position: absolute;
    left: 40px;
    top: 38px;
    display: flex;
    align-items: center;
    gap: 7px;
  }
  .brand-dot {
    width: 16px;
    height: 16px;
    border-radius: 50%;
    background: var(--brand);
  }
  .brand-name {
    font-size: 17px;
    font-weight: 400;
    letter-spacing: 0.5px;
    color: var(--brand);
  }
  .watermark {
    position: absolute;
    left: 250px;
    top: 690px;
    width: 92px;
    height: 92px;
    border-radius: 50%;
    background: var(--watermark);
  }
  .details {
    position: absolute;
    font-size: 10.5px;
    line-height: 15px;
    color: var(--label);
    margin: 0;
    white-space: nowrap;
  }
  .details b {
    color: var(--value);
    font-weight: 700;
  }
  .details-finance {
    left: 40px;
    top: 722px;
  }
  .details-address {
    left: 300px;
    top: 800px;
  }
</style>
</head>
<body>
  <main class="sheet">
    <header class="brand">
      <span class="brand-dot"></span>
      <span class="brand-name">VOLTRINA</span>
    </header>

    <div class="watermark"></div>

    <p class="details details-finance">
      VAT TAX <b>DE5704168</b><br>
      Bank Account: <b>Norrfeld Bank</b><br>
      IBAN <b>DE421705238ß310482</b><br>
      Swift: <b>KOLV3154802</b> <b>EORI 3041296587</b><br>
      Company Number: <b>HRB 61508</b>
    </p>

    <p class="details details-address">
      Adress: <b>VOLTRINA UG Amsel Strasse 7</b><br>
      Postal Code <b>04683</b><br>
      City Halvenstedt Country: <b>Germany</b><br>
      Email: <b>info@voltrina-example.com</b>
    </p>
  </main>
</body>
</html>
```